Claim Advocates Circle Business card

We need to get business card Design for our Company we are Public Adjusters in Chicago Illinois - i like to see good combination and elements from my Company Logo. as well To be an two side design

Target Market(s)

Home /Business owner Property Managers

Industry/Entity Type

Business

Contact Information for Business Card

to show the Element of our logo i will Like 3D

Font styles to use
Sans Serif

Requirements
Must have
• Logo and Element of the Logo in 3D
Nice to have
• Logo That we Provide 3D Same Colors or open for suggestions
Should not have
• unleare view -

```html
<!DOCTYPE html>
<html lang="en">
<head>
<meta charset="utf-8">
<title>Claim Advocates Circle – Business Card</title>
<link href="https://fonts.googleapis.com/css2?family=Open+Sans:wght@400;600;700&display=swap" rel="stylesheet">
<style>
  :root {
    --page-bg: #e6e6e6;
    --card-white: #ffffff;
    --brand-navy: #1a22a8;
    --brand-orange: #e0583a;
    --text-gray: #555555;
    --rule: #3c3f8f;
  }
  * { margin: 0; padding: 0; box-sizing: border-box; }
  html, body {
    width: 1105px; height: 1200px; overflow: hidden;
    background: var(--page-bg);
    font-family: "Open Sans", Arial, sans-serif;
  }
  .card {
    position: absolute; left: 192px;
    width: 720px; height: 412px;
    box-shadow: 0 4px 14px rgba(0,0,0,0.25);
    overflow: hidden;
  }
  .card-front { top: 146px; background: var(--card-white); }
  .card-back { top: 602px; background: var(--brand-orange); }

  .front-brand {
    position: absolute; right: 37px; top: 38px;
    display: flex; align-items: center; gap: 14px;
  }
  .brand-dot {
    width: 80px; height: 80px; border-radius: 50%;
    background: var(--brand-navy);
  }
  .brand-name {
    font-weight: 700; font-size: 24px; color: var(--brand-navy);
    white-space: nowrap;
  }

  .person-name {
    position: absolute; left: 36px; top: 186px;
    font-size: 25px; font-weight: 600; color: var(--brand-navy);
    letter-spacing: 0.5px;
  }
  .person-title {
    position: absolute; left: 36px; top: 218px;
    font-size: 19px; color: var(--brand-orange);
  }
  .divider {
    position: absolute; left: 36px; top: 250px;
    width: 640px; height: 2px; background: var(--rule);
  }
  .contact-list {
    position: absolute; left: 36px; top: 264px;
    list-style: none;
  }
  .contact-list li {
    display: flex; align-items: center; gap: 8px;
    height: 27.5px;
    font-size: 19px; color: var(--text-gray);
  }
  .contact-list li.email { font-size: 17px; }
  .contact-list svg { width: 20px; height: 20px; fill: var(--brand-navy); flex: none; }

  .address {
    position: absolute; right: 37px; top: 296px;
    text-align: right; font-size: 18px; color: var(--text-gray);
    line-height: 26px;
  }
  .address .web { letter-spacing: 3px; font-size: 17px; }

  .front-band { position: absolute; left: 0; bottom: 0; width: 720px; height: 16px; }

  .back-brand {
    position: absolute; left: 0; right: 0; top: 80px;
    display: flex; flex-direction: column; align-items: center; gap: 22px;
  }
  .back-brand .brand-dot { width: 150px; height: 150px; background: var(--card-white); }
  .back-brand .brand-name { color: var(--card-white); font-size: 30px; }
  .back-web {
    position: absolute; left: 0; right: 0; top: 346px;
    text-align: center; color: var(--card-white);
    font-size: 18px; letter-spacing: 3px;
  }
</style>
</head>
<body>

<section class="card card-front">
  <div class="front-brand">
    <span class="brand-dot"></span>
    <span class="brand-name">Claim Advocates Circle</span>
  </div>

  <div class="person-name">MARK LENNER</div>
  <div class="person-title">President</div>
  <div class="divider"></div>

  <ul class="contact-list">
    <li>
      <svg viewBox="0 0 24 24"><path d="M3 9c0-3 4-5 9-5s9 2 9 5v2h-5V9H8v2H3zM6 12h12l2 8H4z"/></svg>
      312 555 0147
    </li>
    <li>
      <svg viewBox="0 0 24 24"><path d="M7 1h10a2 2 0 0 1 2 2v18a2 2 0 0 1-2 2H7a2 2 0 0 1-2-2V3a2 2 0 0 1 2-2zm0 3v14h10V4zm5 15.5a1 1 0 1 0 0 2 1 1 0 0 0 0-2z"/></svg>
      312 555 0182
    </li>
    <li>
      <svg viewBox="0 0 24 24"><path d="M6 2h12v6H6zM3 9h18v9h-3v4H6v-4H3zm5 6v5h8v-5z"/></svg>
      312 555 0199
    </li>
    <li class="email">
      <svg viewBox="0 0 24 24"><path d="M2 5h20v14H2zm2 2v1l8 5 8-5V7l-8 5z"/></svg>
      mark@claimcircle.com
    </li>
  </ul>

  <div class="address">
    <div>4120 Harlow Avenue</div>
    <div>Chicago, IL 60614</div>
    <div class="web">www.claimcircle.com</div>
  </div>

  <svg class="front-band" viewBox="0 0 720 16" preserveAspectRatio="none">
    <defs>
      <linearGradient id="band-blue" x1="0" x2="1">
        <stop offset="0" stop-color="#2a3fe0"/>
        <stop offset="0.5" stop-color="#13208f"/>
        <stop offset="1" stop-color="#0b1260"/>
      </linearGradient>
    </defs>
    <polygon points="0,0 395,0 390,16 0,16" fill="url(#band-blue)"/>
    <polygon points="400,0 720,0 720,16 394,16" fill="var(--brand-orange)"/>
  </svg>
</section>

<section class="card card-back">
  <div class="back-brand">
    <span class="brand-dot"></span>
    <span class="brand-name">Claim Advocates Circle</span>
  </div>
  <div class="back-web">www.ClaimAdvocatesCircle.com</div>
</section>

</body>
</html>
```